Business Cards for new orthopaedic surgery practice

My husband and I are starting our own orthopaedic surgery practice. We are looking for a business card that is uniform, but one will have my name/title and the other will have his. You can just create one design with my name on it for now. But when I choose your design as the winning design I will ask that you add another copy with his name/title.

We are looking for classy, simple, elite all in one. We like dark blues/a little gold/yellow. Something that goes with our logo. We want our logo incorporated. Here is all the info you need:
Business name: RV Spine & Vitality Center
Location: 38915 North Bramble Ave
Maple Hollow, FL 33480
Phone: 954-218-4630
Fax: 954-571-2846
Email: info@myrvspine.example

Names: Lucinda Ferrow, M.D.
Board Certified Hand and Upper Extremity Surgeon

Emeka Dlunga, M.D.
Board Certified Hip & Knee Replacement/General Orthopaedic Surgeon

Can decide what you want to put on the back. Maybe a slogan:
Grounded in Care. Centered on You

I am just going to upload our logo. The only thing is if we select you as the winning design, the location, and phone numbers may change. We will need your help to update that once fully solidified.

Industry/Entity Type

Medical

Contact Information for Business Card

Colors
0054AA
0677BA
7BADD7
CADEEF
E8F1F8
0094D4
00A9DD
6FCCEA
C7EBF8
E9F6FB

Requirements
Must have
• class, appeal,
Should not have
• We want to air on the side of masculine if we are looking at masculine vs. feminine feel. But we still want it classy, sophisticated, and something we will love

```html
<!DOCTYPE html>
<html lang="en">
<head>
<meta charset="utf-8">
<title>RV Spine &amp; Vitality Center — Business Card</title>
<link rel="stylesheet" href="https://fonts.googleapis.com/css2?family=Marcellus&family=Lora:wght@400;500&display=swap">
<style>
  :root {
    --navy: #16254f;
    --navy-deep: #0f1c40;
    --gold: #c9a24f;
    --gold-soft: #d4b06a;
    --white: #ffffff;
    --paper: #fbfbf9;
    --ink: #1a2246;
    --backdrop: #e9ebef;
  }
  * { margin: 0; padding: 0; box-sizing: border-box; }
  html, body { width: 1200px; height: 900px; overflow: hidden; }
  body {
    background: var(--backdrop);
    font-family: "Lora", Georgia, serif;
    color: var(--ink);
    position: relative;
  }
  .card {
    position: absolute;
    left: 250px;
    width: 700px;
    height: 400px;
    overflow: hidden;
    box-shadow: 0 10px 28px rgba(15, 28, 64, 0.18);
  }
  .card-back { top: 30px; background: var(--navy); }
  .card-front { top: 465px; background: var(--paper); }

  .brand {
    position: absolute;
    display: flex;
    align-items: center;
    gap: 14px;
  }
  .brand-circle {
    width: 50px; height: 50px;
    border-radius: 50%;
    border: 2px solid currentColor;
    flex: none;
  }
  .brand-name {
    font-family: "Marcellus", Georgia, serif;
    font-size: 20px;
    line-height: 1.2;
    letter-spacing: 1px;
    text-transform: uppercase;
    width: 170px;
  }
  .card-back .brand { left: 255px; top: 100px; color: var(--white); }
  .card-front .brand { left: 40px; top: 150px; color: var(--navy); }

  .slogan {
    position: absolute;
    left: 0; right: 0;
    top: 258px;
    text-align: center;
    font-family: "Lora", Georgia, serif;
    font-weight: 500;
    font-size: 34px;
    color: var(--gold);
  }

  .identity {
    position: absolute;
    right: 44px;
    top: 44px;
    text-align: right;
  }
  .person-name {
    font-family: "Marcellus", Georgia, serif;
    font-weight: 400;
    font-size: 44px;
    color: var(--navy);
    letter-spacing: 0.5px;
    line-height: 1.1;
  }
  .person-title {
    font-size: 14px;
    font-weight: 500;
    color: var(--gold);
    margin-top: 6px;
  }

  .contact-list {
    position: absolute;
    right: 44px;
    top: 140px;
    list-style: none;
  }
  .contact-list li {
    display: flex;
    justify-content: flex-end;
    align-items: center;
    gap: 10px;
    font-size: 15px;
    color: var(--ink);
    height: 28px;
  }
  .contact-list svg { width: 16px; height: 16px; fill: var(--gold); flex: none; }

  .bottom-strip {
    position: absolute;
    left: 0; right: 0; bottom: 0;
    height: 28px;
    background: var(--navy);
  }
  .address-band {
    position: absolute;
    right: 0; bottom: 0;
    width: 340px;
    height: 122px;
    background: var(--navy);
    clip-path: polygon(24px 0, 100% 0, 100% 100%, 0 100%);
  }
  .address-street {
    position: absolute;
    right: 44px; top: 26px;
    font-size: 21px;
    color: var(--white);
    display: flex; align-items: center; gap: 10px;
    white-space: nowrap;
  }
  .address-street svg { width: 18px; height: 18px; fill: var(--gold); flex: none; }
  .city-band {
    position: absolute;
    left: 0; bottom: 28px;
    width: 350px;
    height: 56px;
    background: var(--gold-soft);
    display: flex; align-items: center;
    padding-left: 40px;
    font-size: 21px;
    color: var(--navy-deep);
    white-space: nowrap;
  }
</style>
</head>
<body>

<section class="card card-back" aria-label="Card back">
  <div class="brand">
    <span class="brand-circle"></span>
    <span class="brand-name">RV Spine &amp; Vitality Center</span>
  </div>
  <p class="slogan">Grounded in Care. Centered on You</p>
</section>

<section class="card card-front" aria-label="Card front">
  <div class="identity">
    <h1 class="person-name">Lucinda Ferrow, M.D.</h1>
    <p class="person-title">Board Certified Hand and Upper Extremity Surgeon</p>
  </div>

  <ul class="contact-list">
    <li>954-218-4630
      <svg viewBox="0 0 24 24" aria-hidden="true"><path d="M6.6 10.8a15.1 15.1 0 0 0 6.6 6.6l2.2-2.2c.3-.3.7-.4 1-.2 1.1.4 2.3.6 3.6.6.6 0 1 .4 1 1V20c0 .6-.4 1-1 1A17 17 0 0 1 3 4c0-.6.4-1 1-1h3.5c.6 0 1 .4 1 1 0 1.3.2 2.5.6 3.6.1.3 0 .7-.2 1z"/></svg>
    </li>
    <li>954-571-2846
      <svg viewBox="0 0 24 24" aria-hidden="true"><path d="M7 3h10v5H7zM4 9h16a2 2 0 0 1 2 2v6h-4v4H6v-4H2v-6a2 2 0 0 1 2-2zm4 7v3h8v-3z"/></svg>
    </li>
    <li>info@myrvspine.example
      <svg viewBox="0 0 24 24" aria-hidden="true"><path d="M2 5h20v14H2zm2 2v.5l8 5 8-5V7l-8 5z"/></svg>
    </li>
  </ul>

  <div class="brand">
    <span class="brand-circle"></span>
    <span class="brand-name">RV Spine &amp; Vitality Center</span>
  </div>

  <div class="bottom-strip"></div>
  <div class="address-band">
    <p class="address-street">38915 North Bramble Ave
      <svg viewBox="0 0 24 24" aria-hidden="true"><path d="M12 2a7 7 0 0 0-7 7c0 5 7 13 7 13s7-8 7-13a7 7 0 0 0-7-7zm0 9.5A2.5 2.5 0 1 1 12 6.5a2.5 2.5 0 0 1 0 5z"/></svg>
    </p>
  </div>
  <div class="city-band">Maple Hollow, FL 33480</div>
</section>

</body>
</html>
```